Marrowgate Auctions Business Cards Design Needed

I need a business card design that is modern looking - double sided (maybe just my logo on the back, but open to suggestions) - the overall design is up to you. I want it to be easy to read - not over the top flashy. I already have a company logo which I uploaded so that needs to be used. The colors of my logo are the colors I want on the card... so blue and gray (do need to match the logo colors).

Requirements
Must have
• Would like the card to be sleek, modern and easy to ready

```html
<!DOCTYPE html>
<html lang="en">
<head>
<meta charset="utf-8">
<title>Marrowgate Auctions – Business Cards</title>
<link href="https://fonts.googleapis.com/css2?family=Lato:wght@400;700;900&display=swap" rel="stylesheet">
<style>
  :root {
    --stage: #2b2b2d;
    --card-dark: #58595b;
    --card-light: #ffffff;
    --brand-blue: #2f74c0;
    --ink-gray: #4b4b4d;
    --band-gray: #5c5d60;
  }
  * { box-sizing: border-box; margin: 0; padding: 0; }
  html, body { width: 1200px; height: 900px; overflow: hidden; }
  body {
    background: var(--stage);
    font-family: "Lato", sans-serif;
    position: relative;
  }
  .card {
    position: absolute;
    left: 250px;
    width: 700px;
    height: 400px;
    border-radius: 3px;
    box-shadow: 0 10px 30px rgba(0,0,0,.45);
    overflow: hidden;
  }
  /* back side */
  .card-back {
    top: 35px;
    background: var(--card-dark);
    display: flex;
    flex-direction: column;
    align-items: center;
    justify-content: center;
    color: #fff;
  }
  .brand {
    display: flex;
    align-items: center;
    gap: 14px;
  }
  .brand-mark {
    width: 34px; height: 34px;
    background: var(--brand-blue);
  }
  .brand-name {
    font-weight: 900;
    text-transform: uppercase;
    letter-spacing: .02em;
  }
  .card-back .brand-name { font-size: 46px; color: #fff; }
  .card-back .tagline {
    margin-top: 10px;
    font-size: 22px;
    font-weight: 700;
    letter-spacing: .01em;
  }
  /* front side */
  .card-front {
    top: 465px;
    background: var(--card-light);
    color: var(--ink-gray);
  }
  .card-front .brand {
    position: absolute;
    top: 52px;
    right: 44px;
  }
  .card-front .brand-mark { width: 26px; height: 26px; }
  .card-front .brand-name { font-size: 30px; color: var(--ink-gray); }
  .person {
    position: absolute;
    left: 48px;
    top: 118px;
  }
  .person-name { font-size: 30px; font-weight: 700; }
  .person-role { font-size: 18px; color: var(--brand-blue); margin-top: 4px; }
  .person-place { font-size: 20px; margin-top: 4px; }
  .contact {
    position: absolute;
    left: 48px;
    top: 252px;
    list-style: none;
  }
  .contact li {
    display: flex;
    align-items: center;
    gap: 14px;
    font-size: 21px;
    height: 32px;
  }
  .contact svg { width: 20px; height: 20px; fill: var(--brand-blue); flex: none; }
  .card-front .tagline {
    position: absolute;
    right: 44px;
    bottom: 46px;
    text-align: right;
    font-size: 21px;
    line-height: 1.3;
    color: var(--brand-blue);
  }
  .card-band {
    position: absolute;
    left: 0; right: 0; bottom: 0;
    height: 16px;
    background: var(--band-gray);
  }
</style>
</head>
<body>

<section class="card card-back" aria-label="Card back">
  <div class="brand">
    <span class="brand-mark"></span>
    <span class="brand-name">Marrowgate Auctions</span>
  </div>
  <p class="tagline">Improving Charity Auctions Nationwide</p>
</section>

<section class="card card-front" aria-label="Card front">
  <div class="brand">
    <span class="brand-mark"></span>
    <span class="brand-name">Marrowgate Auctions</span>
  </div>

  <div class="person">
    <p class="person-name">Owen Talbridge</p>
    <p class="person-role">Owner | President - Auctioneer</p>
    <p class="person-place">Cedarmoor, Washington, USA</p>
  </div>

  <ul class="contact">
    <li>
      <svg viewBox="0 0 24 24" aria-hidden="true"><path d="M6.6 10.8a15.1 15.1 0 0 0 6.6 6.6l2.2-2.2a1 1 0 0 1 1-.25 11.4 11.4 0 0 0 3.6.57 1 1 0 0 1 1 1V20a1 1 0 0 1-1 1A17 17 0 0 1 3 4a1 1 0 0 1 1-1h3.5a1 1 0 0 1 1 1c0 1.25.2 2.45.57 3.57a1 1 0 0 1-.25 1z"/></svg>
      555-014-2297
    </li>
    <li>
      <svg viewBox="0 0 24 24" aria-hidden="true"><path d="M2 5h20v14H2z M3.5 6.5 12 13l8.5-6.5" fill="none" stroke="var(--brand-blue)" stroke-width="2"/></svg>
      marrowgate@mailbox.com
    </li>
    <li>
      <svg viewBox="0 0 24 24" aria-hidden="true"><g fill="none" stroke="var(--brand-blue)" stroke-width="1.8"><circle cx="12" cy="12" r="9.5"/><ellipse cx="12" cy="12" rx="4" ry="9.5"/><path d="M2.5 12h19M4 7h16M4 17h16"/></g></svg>
      www.bidrevival.com
    </li>
  </ul>

  <p class="tagline">Improving Charity<br>Auctions Nationwide</p>
  <div class="card-band"></div>
</section>

</body>
</html>
```